Quellbrook Supply Chain and Logistic Consulting

Please review the attached Business Card. I want as close to this card with the colors, fonts, and quality of the card as possible. The attached compass should replace the deer head on both sides of the card and the text should say:

Backside
Compass JPEG
Quellbrook Partners
A Supply Chain and Logistics Consulting Company

Frontside
Quellbrook Partners
Ross Pelgrave - Marrow Bay
President
____________________________________
(555) 214-9037
QuellbrookHQ@Mailvento.com
_____________________________________

Bottom Front Side

Target Market(s)

Businesses

Contact Information for Business Card

Backside
Compass JPEG
Quellbrook Partners

Frontside
Quellbrook Partners
President
(555) 214-9037
QuellbrookHQ@Mailvento.com

Bottom Front Side

Font styles to use
Serif
Script

Colors

Designer to choose colors to be used in the design.

Requirements
Must have
• See attached card for reference
Nice to have
Should not have

```html
<!DOCTYPE html>
<html lang="en">
<head>
<meta charset="utf-8">
<title>Quellbrook Partners — Business Card</title>
<link rel="stylesheet" href="https://fonts.googleapis.com/css2?family=Playfair+Display:wght@400;700&family=Crimson+Text:wght@400;600&display=swap">
<style>
  :root {
    --stage: #2b2d30;
    --card: #141414;
    --card-edge: #262626;
    --ink: #e9e9e9;
    --ink-soft: #bdbdbd;
    --rule: #9a9a9a;
    --mark: #d8d8d8;
    --mark-faint: rgba(255,255,255,0.06);
  }
  * { box-sizing: border-box; margin: 0; padding: 0; }
  html, body {
    width: 1200px; height: 900px; overflow: hidden;
    background: var(--stage);
  }
  .stage {
    width: 1200px; height: 900px;
    display: flex; align-items: center; justify-content: center; gap: 40px;
  }
  .card {
    position: relative;
    width: 540px; height: 309px;
    background: var(--card);
    border: 1px solid var(--card-edge);
    border-radius: 4px;
    overflow: hidden;
    color: var(--ink);
    font-family: "Crimson Text", Georgia, serif;
    text-align: center;
  }
  .wordmark {
    font-family: "Playfair Display", Georgia, serif;
    font-weight: 700;
    letter-spacing: 1px;
    color: var(--ink);
    white-space: nowrap;
  }
  .tagline {
    font-size: 11px;
    letter-spacing: 1.2px;
    text-transform: uppercase;
    color: var(--ink-soft);
    white-space: nowrap;
  }
  .ruled {
    display: flex; align-items: center; gap: 12px;
  }
  .ruled::before, .ruled::after {
    content: ""; flex: 1; height: 1px; background: var(--rule);
  }

  /* Front side */
  .card-front .faint-mark {
    position: absolute; right: -70px; bottom: -90px;
    width: 300px; height: 300px;
  }
  .front-body {
    position: relative;
    padding: 30px 40px 0;
  }
  .card-front .wordmark { font-size: 24px; }
  .card-front .tagline { margin-top: 2px; }
  .holder {
    margin-top: 14px;
    font-family: "Playfair Display", Georgia, serif;
    font-weight: 700; font-size: 19px;
  }
  .holder .dot { margin: 0 6px; }
  .role { font-size: 15px; color: var(--ink-soft); margin-top: -2px; }
  .contact-block {
    margin: 10px 40px 0;
    border-top: 1px solid var(--rule);
    border-bottom: 1px solid var(--rule);
    padding: 7px 0 6px;
    font-size: 15px; color: var(--ink);
    white-space: nowrap;
  }
  .contact-block .sep { margin: 0 6px; color: var(--ink-soft); }
  .socials {
    margin-top: 8px;
    font-size: 14px; color: var(--ink);
  }
  .socials .sep { margin: 0 8px; color: var(--ink-soft); }
  .front-foot {
    position: absolute; left: 30px; right: 30px; bottom: 18px;
  }

  /* Back side */
  .card-back .mark {
    position: absolute; left: 50%; top: 46px;
    width: 150px; height: 150px;
    transform: translateX(-10px);
  }
  .back-brand {
    position: absolute; left: 30px; right: 30px; top: 206px;
  }
  .card-back .wordmark { font-size: 22px; }
  .card-back .tagline { margin-top: 4px; }
</style>
</head>
<body>
<main class="stage">

  <section class="card card-front" aria-label="Business card front">
    <svg class="faint-mark" viewBox="0 0 300 300" role="img" aria-label="Faint Quellbrook brand mark area">
      <circle cx="150" cy="150" r="148" fill="var(--mark-faint)"/>
    </svg>
    <div class="front-body">
      <h1 class="wordmark">QUELLBROOK PARTNERS</h1>
      <p class="tagline">A Supply Chain and Logistics Consulting Company</p>
      <p class="holder">Ross Pelgrave<span class="dot">•</span>Marrow Bay</p>
      <p class="role">President</p>
      <p class="contact-block">(555) 214-9037<span class="sep">|</span>QuellbrookHQ@Mailvento.com</p>
      <p class="socials">Friendwall<span class="sep">/</span>Snapgrid</p>
    </div>
    <p class="front-foot tagline ruled">A Supply Chain and Logistics Consulting Company</p>
  </section>

  <section class="card card-back" aria-label="Business card back">
    <svg class="mark" viewBox="0 0 150 150" role="img" aria-label="Quellbrook compass brand mark">
      <circle cx="75" cy="75" r="72" fill="var(--mark)"/>
    </svg>
    <div class="back-brand">
      <h2 class="wordmark ruled">QUELLBROOK PARTNERS</h2>
      <p class="tagline">A Supply Chain and Logistics Consulting Company</p>
    </div>
  </section>

</main>
</body>
</html>
```